Plumbing Truck design, emergency plumbing vehicle

Simple, highly effective plumbing design for plumbing vehicles

Brightwater Plumbing & Gas Services
(The Reliable Plumbing Specialists) moto

yellow, black and white colours (white as the vehicles are already painted white)

Clean and simple design

Attention grabbing

24hr Emergency service (listed on on the vehicle) possibly in red colour

Target Market(s)

plumbing

Industry/Entity Type

Plumbing

Colors
fbed22

Requirements
Must have
• Brightwater Plumbing & Gas Services
• (The Reliable Plumbing Specialists) moto
• yellow, black and white colours (white as the vehicles are already painted white)
• Clean and simple design
• Attention grabbing
• 24hr Emergency service (listed on on the vehicle) possibly in red colour
Should not have
• No plumbing symbols, pictures or icons

```html
<!DOCTYPE html>
<html lang="en">
<head>
<meta charset="utf-8">
<title>Brightwater Plumbing &amp; Gas Services – Vehicle Livery</title>
<link rel="stylesheet" href="https://fonts.googleapis.com/css2?family=Arimo:wght@700&family=Archivo+Narrow:wght@700&display=swap">
<style>
  :root {
    --livery-yellow: #f2f21a;
    --livery-black: #0d0d0d;
    --livery-white: #ffffff;
    --livery-red: #d50f14;
    --backdrop: #e9eaec;
    --text-light: #e6e6e6;
  }
  * { margin: 0; padding: 0; box-sizing: border-box; }
  html, body { width: 1200px; height: 925px; overflow: hidden; background: var(--backdrop); }
  .canvas { position: relative; width: 1200px; height: 925px; font-family: "Arimo", Arial, sans-serif; font-weight: 700; }
  .shapes { position: absolute; inset: 0; }
  .txt { position: absolute; white-space: nowrap; }

  .headline { font-family: "Archivo Narrow", "Arial Narrow", sans-serif; font-weight: 700; color: var(--livery-black); }
  .headline .accent { color: var(--livery-red); }

  .side-headline { left: 665px; width: 510px; top: 72px; text-align: center; font-size: 46px; }
  .side-response { left: 665px; width: 510px; top: 164px; text-align: center; font-size: 36px; color: var(--text-light); font-family: "Arimo", Arial, sans-serif; }
  .side-web { left: 665px; width: 510px; top: 250px; text-align: center; font-size: 16px; color: var(--livery-black); }

  .brand-name { color: var(--livery-black); text-align: center; line-height: 1.15; font-size: 24px; }
  .cab-brand { left: 315px; width: 270px; top: 215px; white-space: normal; }
  .rear-brand { left: 480px; width: 240px; top: 672px; white-space: normal; font-size: 22px; }

  .tagline { color: var(--text-light); font-size: 19px; text-align: center; }
  .cab-tagline { left: 265px; width: 365px; top: 317px; }
  .rear-tagline { left: 443px; width: 317px; top: 780px; font-size: 18px; }

  .rear-emergency { left: 335px; width: 170px; top: 552px; text-align: center; font-size: 31px; line-height: 1.18; }
  .rear-response { left: 700px; width: 160px; top: 558px; text-align: center; font-size: 26px; line-height: 1.25; color: var(--livery-black); font-family: "Arimo", Arial, sans-serif; }
</style>
</head>
<body>
<main class="canvas">
  <svg class="shapes" width="1200" height="925" viewBox="0 0 1200 925" aria-hidden="true">
    <!-- cab door panel -->
    <rect class="cab-panel" x="0" y="60" width="650" height="300" fill="var(--livery-white)"/>
    <path class="cab-yellow" d="M0 250 Q120 215 250 210 L650 210 L650 360 L0 360 Z" fill="var(--livery-yellow)"/>
    <rect class="cab-tagline-band" x="265" y="312" width="365" height="32" rx="16" fill="var(--livery-black)"/>
    <!-- tray panel -->
    <rect class="tray-panel" x="665" y="50" width="510" height="300" fill="var(--livery-yellow)"/>
    <rect class="tray-response-band" x="665" y="150" width="510" height="72" fill="var(--livery-black)"/>
    <!-- rear panel -->
    <rect class="rear-panel" x="333" y="510" width="530" height="340" rx="6" fill="var(--livery-yellow)"/>
    <rect class="rear-tagline-band" x="443" y="775" width="317" height="30" fill="var(--livery-black)"/>
  </svg>

  <!-- side view -->
  <p class="txt brand-name cab-brand">BRIGHTWATER PLUMBING &amp; GAS SERVICES</p>
  <p class="txt tagline cab-tagline">The Reliable Plumbing Specialists</p>
  <p class="txt headline side-headline"><span class="accent">24/7 EMERGENCY</span> SERVICE</p>
  <p class="txt side-response">RAPID RESPONSE</p>
  <p class="txt side-web">BrightwaterPlumbing.com.au</p>

  <!-- rear view -->
  <p class="txt headline rear-emergency"><span class="accent">24/7<br>EMERGENCY</span><br>SERVICE</p>
  <p class="txt rear-response">RAPID<br>RESPONSE</p>
  <p class="txt brand-name rear-brand">BRIGHTWATER PLUMBING &amp; GAS SERVICES</p>
  <p class="txt tagline rear-tagline">The Reliable Plumbing Specialists</p>
</main>
</body>
</html>
```